Executive Business Card for Healthcare Company [Need Today]

I need a business card design for a healthcare company. The only branding the company has thus far is a logo. The cards will be utilized by company executives. The design I envision will be vibrant and appealing but with a corporate feel. They shouldn't be too casual or playful. I would like to complete this project TODAY if possible.

Target Market(s)

Healthcare vendors, other executives in healthcare and pharmaceuticals

Industry/Entity Type

Pharmaceutical

Contact Information for Business Card

See attachment

Font styles to use
Serif
Sans Serif

Colors

Designer to choose colors to be used in the design.

```html
<!DOCTYPE html>
<html lang="en">
<head>
<meta charset="utf-8">
<title>Corvane Therapeutics – Business Card</title>
<link rel="stylesheet" href="https://fonts.googleapis.com/css2?family=Cinzel:wght@700&family=Open+Sans:wght@300;400&family=Tinos&display=swap">
<style>
  :root {
    --backdrop: #8fa6ad;
    --card-center: #ffffff;
    --card-edge: #d6d7db;
    --teal: #2fb8b8;
    --neutral-block: #d3d6da;
    --icon-bg: #8fd3c6;
    --ink: #5a5a5c;
    --ink-dark: #1e1e1e;
  }
  html, body {
    margin: 0;
    width: 1200px;
    height: 800px;
    overflow: hidden;
    background: var(--backdrop);
  }
  .canvas { position: relative; width: 1200px; height: 800px; }
  .card {
    position: absolute;
    left: 326px;
    width: 538px;
    height: 307px;
    overflow: hidden;
  }
  .card--front { top: 24px; }
  .card--back { top: 426px; }
  .card__texture {
    position: absolute; inset: 0;
    background: radial-gradient(ellipse at 50% 50%, var(--card-center) 35%, #eeeef0 65%, var(--card-edge) 100%);
  }
  .brand { position: absolute; display: flex; align-items: center; }
  .brand__mark {
    background: var(--neutral-block);
    flex: none;
  }
  .brand__rule { width: 1px; background: #8a8a8a; flex: none; }
  .brand__name {
    font-family: "Open Sans", sans-serif;
    font-weight: 300;
    color: var(--teal);
    line-height: 1;
  }
  .brand--front { left: 152px; top: 80px; }
  .brand--front .brand__mark { width: 100px; height: 100px; }
  .brand--front .brand__rule { height: 54px; margin: 0 12px 0 18px; }
  .brand--front .brand__name { font-size: 40px; }
  .brand--front .brand__name small { display: block; font-size: 24px; text-align: right; margin-top: 6px; }
  .brand--back { left: 12px; top: 120px; }
  .brand--back .brand__mark { width: 60px; height: 60px; }
  .brand--back .brand__rule { height: 34px; margin: 0 7px 0 10px; }
  .brand--back .brand__name { font-size: 25px; }
  .brand--back .brand__name small { display: block; font-size: 15px; text-align: right; margin-top: 4px; }
  .find-us {
    position: absolute; left: 0; right: 0; top: 201px; margin: 0;
    text-align: center;
    font-family: "Tinos", serif;
    font-size: 17px;
    color: var(--ink-dark);
  }
  .social-row {
    position: absolute; left: 0; right: 0; top: 230px;
    display: flex; justify-content: center; gap: 9px;
  }
  .social-row span { width: 17px; height: 17px; background: var(--teal); border-radius: 2px; }
  .divider {
    position: absolute; left: 241px; top: 70px;
    width: 2px; height: 164px; background: var(--teal);
  }
  .person { position: absolute; left: 294px; top: 40px; }
  .person__name {
    font-family: "Cinzel", serif; font-weight: 700;
    font-size: 23px; letter-spacing: 1.5px; color: var(--ink);
    margin: 0;
  }
  .person__title {
    font-family: "Cinzel", serif; font-weight: 700;
    font-size: 10.5px; letter-spacing: 1.2px; color: var(--ink);
    margin: 2px 0 0 2px;
  }
  .contact { position: absolute; left: 291px; top: 109px; margin: 0; padding: 0; list-style: none; }
  .contact__item { position: relative; display: flex; align-items: flex-start; height: 36px; }
  .contact__icon {
    width: 26px; height: 26px; border-radius: 50%;
    background: var(--icon-bg); flex: none;
    display: flex; align-items: center; justify-content: center;
    margin-right: 9px;
  }
  .contact__text { font-family: "Open Sans", sans-serif; font-size: 13px; color: var(--ink); line-height: 26px; }
  .contact__text--large { font-size: 16px; }
  .contact__text--serif { font-family: "Tinos", serif; font-size: 15px; line-height: 19px; margin-top: 3px; }
</style>
</head>
<body>
<main class="canvas">

  <section class="card card--front">
    <div class="card__texture" role="img" aria-label="Soft silver dot texture fading to white at the centre"></div>
    <div class="brand brand--front">
      <span class="brand__mark"></span>
      <span class="brand__rule"></span>
      <span class="brand__name">Corvane<small>Therapeutics</small></span>
    </div>
    <p class="find-us">Find Us on:</p>
    <div class="social-row" role="img" aria-label="Social network links">
      <span></span><span></span><span></span><span></span>
    </div>
  </section>

  <section class="card card--back">
    <div class="card__texture" role="img" aria-label="Soft silver dot texture fading to white at the centre"></div>
    <div class="brand brand--back">
      <span class="brand__mark"></span>
      <span class="brand__rule"></span>
      <span class="brand__name">Corvane<small>Therapeutics</small></span>
    </div>
    <div class="divider"></div>
    <div class="person">
      <h1 class="person__name">Daniel Mercer</h1>
      <p class="person__title">Senior Director of Marketing</p>
    </div>
    <ul class="contact">
      <li class="contact__item">
        <span class="contact__icon"><svg width="14" height="10" viewBox="0 0 14 10"><rect x="0.5" y="0.5" width="13" height="9" fill="none" stroke="#fff"/><path d="M0.5 0.5 L7 6 L13.5 0.5" fill="none" stroke="#fff"/></svg></span>
        <span class="contact__text">dmercer@corvanerx.com</span>
      </li>
      <li class="contact__item">
        <span class="contact__icon"><svg width="14" height="12" viewBox="0 0 14 12"><path d="M1 4 Q7 -1 13 4 L11 5 L10 3.5 Q7 2.5 4 3.5 L3 5 Z" fill="#fff"/><rect x="3" y="6" width="8" height="5" rx="1" fill="#fff"/></svg></span>
        <span class="contact__text">555-201-4473</span>
      </li>
      <li class="contact__item">
        <span class="contact__icon"><svg width="13" height="13" viewBox="0 0 13 13"><path d="M2 1 L4.5 1 L5.5 4 L4 5.2 Q5.5 8 8 9 L9.2 7.5 L12 8.5 L12 11 Q11 12.5 9 12 Q2.5 10 1 3.5 Q0.8 1.8 2 1 Z" fill="#fff"/></svg></span>
        <span class="contact__text contact__text--large">555-201-8816</span>
      </li>
      <li class="contact__item">
        <span class="contact__icon"><svg width="10" height="14" viewBox="0 0 10 14"><path d="M5 0.5 A4.5 4.5 0 0 1 9.5 5 Q9.5 8 5 13.5 Q0.5 8 0.5 5 A4.5 4.5 0 0 1 5 0.5 Z" fill="#fff"/><circle cx="5" cy="5" r="1.7" fill="#8fd3c6"/></svg></span>
        <span class="contact__text contact__text--serif">118 N Linden<br>Street Marlow GA 30299</span>
      </li>
    </ul>
  </section>

</main>
</body>
</html>
```